Design the packaging for a wholesale/retail Date fruit company

We need a box designed for a dates fruit box. This will be used for the wholesale packaging. The brand is called Al Serwa Dates , it is a new business. Al Serwa means the home. It will be part of a food exporting business called Al Serwa Foods. It will be based out of the Middle East and the Holy Lands. Recently Qatar had a grand meet and one of their stadiums was also called Al Serwa, it was designed to represent an Arabian tent. The logo hasn't been designed yet but something simple is fine. I also have a sample design, you can use most of the information from. The product is a Product of Palestine, it is in 5kg boxes the nutritional information is on the sample.

The company is called Tariq Halloum General Trading (THGT) based in Doha Qatar. Logo is provided.

The exporter details are on the sample box.
Use this companies packaging as inspiration for what we are looking to compete with https://qimrana.com/

I require the illustrator/photoshop files please so that we can update details on it.

Industry/Entity Type

food (dates)

Requirements
Must have
• English & Arabic text
Nice to have
• try and incorporate the colour CFB53B

```html
<!DOCTYPE html>
<html lang="en">
<head>
<meta charset="utf-8">
<title>Al Serwa Dates – Medjool Box Front</title>
<link rel="stylesheet" href="https://fonts.googleapis.com/css2?family=Cinzel:wght@400;700&family=Cairo:wght@400&family=Montserrat:wght@600&display=swap">
<style>
  :root {
    --page-bg: #c9c9cd;
    --royal-purple: #4a1a6e;
    --deep-purple: #36104f;
    --cream-light: #f7ecd2;
    --cream-dark: #e6d3a6;
    --gold: #cfb53b;
    --gold-light: #ecd19a;
    --gold-deep: #a9782a;
    --date-light: #d9743a;
    --date-dark: #7a2c12;
    --ink: #1b1b1b;
  }
  html, body {
    margin: 0;
    padding: 0;
    width: 1200px;
    height: 859px;
    overflow: hidden;
    background: var(--page-bg);
  }
  .box-front {
    position: absolute;
    left: 60px;
    top: 23px;
    width: 1080px;
    height: 813px;
    display: block;
  }
  .arabic-title {
    font-family: "Cairo", sans-serif;
    font-size: 38px;
    fill: var(--gold-light);
  }
  .product-title {
    font-family: "Cinzel", serif;
    font-weight: 400;
    font-size: 56px;
    fill: var(--gold-light);
    letter-spacing: 1px;
  }
  .brand-name {
    font-family: "Cinzel", serif;
    font-weight: 700;
    font-size: 56px;
    fill: var(--royal-purple);
  }
  .net-weight {
    font-family: "Montserrat", sans-serif;
    font-weight: 600;
    font-size: 24px;
    fill: var(--ink);
  }
</style>
</head>
<body>
<svg class="box-front" viewBox="0 0 1047 788" xmlns="http://www.w3.org/2000/svg">
  <defs>
    <linearGradient id="creamFill" x1="0" y1="0" x2="0" y2="1">
      <stop offset="0" stop-color="var(--cream-dark)"/>
      <stop offset="0.5" stop-color="var(--cream-light)"/>
      <stop offset="1" stop-color="var(--cream-dark)"/>
    </linearGradient>
    <radialGradient id="purpleFill" cx="0.5" cy="0.35" r="0.8">
      <stop offset="0" stop-color="var(--royal-purple)"/>
      <stop offset="1" stop-color="var(--deep-purple)"/>
    </radialGradient>
    <linearGradient id="goldBand" x1="0" y1="0" x2="1" y2="0">
      <stop offset="0" stop-color="var(--gold-deep)"/>
      <stop offset="0.3" stop-color="var(--gold-light)"/>
      <stop offset="0.6" stop-color="var(--gold)"/>
      <stop offset="1" stop-color="var(--gold-deep)"/>
    </linearGradient>
    <radialGradient id="datesFill" cx="0.5" cy="0.45" r="0.6">
      <stop offset="0" stop-color="var(--date-light)"/>
      <stop offset="1" stop-color="var(--date-dark)"/>
    </radialGradient>
  </defs>

  <rect class="cream-panel" x="0" y="0" width="1047" height="788" fill="url(#creamFill)"/>

  <path class="purple-header" fill="url(#purpleFill)"
        d="M0,0 H1047 V282 C960,330 820,350 700,370 C620,382 580,395 552,408 C520,380 480,360 420,345 C300,320 150,300 0,282 Z"/>
  <path class="gold-band" fill="none" stroke="url(#goldBand)" stroke-width="8"
        d="M0,282 C150,300 300,320 420,345 C480,360 520,380 552,408 C580,395 620,382 700,370 C820,350 960,330 1047,282"/>

  <text class="arabic-title" x="523" y="82" text-anchor="middle" direction="rtl">تمر مجول فلسطيني</text>
  <text class="product-title" x="523" y="163" text-anchor="middle">MEDJOOL DATES</text>
  <text class="product-title" x="523" y="228" text-anchor="middle">NATURAL SWEETNESS</text>

  <g class="brand-lockup">
    <text class="brand-name" x="300" y="418" text-anchor="middle">AL SERWA</text>
    <text class="brand-name" x="300" y="478" text-anchor="middle">DATES</text>
  </g>

  <path class="dates-photo" role="img" aria-label="Photograph of a pile of glossy Medjool dates"
        fill="url(#datesFill)"
        d="M300,620 C290,560 360,520 440,525 C480,470 560,445 640,455 C720,440 800,470 850,500 C930,500 1010,540 1012,610 C1015,690 950,745 860,740 C760,750 640,752 540,740 C430,735 310,700 300,620 Z"/>

  <text class="net-weight" x="55" y="714">5 kg / 11 LBS NET</text>
</svg>
</body>
</html>
```